Hair Extension Packaging

Update 2/16 - please keep submissions coming, I have no front runners yet. Thanks.

I need some new packaging designed for hair extensions. I have enclose pictures of what other companies packaging looks like and a few pictures of some inspiration. I am looking for a packaging that will appeal to a 20's-30's year old demographic and I like things along the lines of glamor/lace/vintage/boudoir/damask inspired. I am going to leave colors up to your creativity for the sample artwork and ask for changes if needed. Id like the design to be a standout but not loud.

The working name for this hair is "Vexa"
Additional Text that I would like on the packaging "100% Premium Virgin Remy Human Hair"

Please keep in mind that the background of the packaging will have many different colors laying over it so be mindful of what the color you chose can effect the hair color in the packaging - no red or orange which can make the hair appear very warm and clash with ashy colors.

Working dimensions for the sample are 22" long, 3" wide.

****Once I decide on the front of the packaging I will also need the back designed which will consist of similar design as the front but with hair care instructions printed on it.***** This finished product must include front and back artwork, open Photoshop files, and additional bleed room for printing. I don't want to waste anyone's time so once I get a front design I like I will work with that artist to create the back.

Please message me with any questions.
Updates

Project Deadline Extended
Reason: Finalizing final choices. Thanks for your submissions!

Target Market(s)

Women in there 20"s - 30's. High fashion, luxurious, glamour

Industry/Entity Type

Hair

Font styles to use
Serif
Script

Requirements
Must have
• Id love the product name to be in script and then mixed with regular font (see the makeup logo example I enclosed)
Should not have
• Should not be masculine. Forget the blue and green colors

```html
<!DOCTYPE html>
<html lang="en">
<head>
<meta charset="utf-8">
<title>Vexa Hair Extension Header Card</title>
<link rel="stylesheet" href="https://fonts.googleapis.com/css2?family=Great+Vibes&family=Playfair+Display:wght@400;700&display=swap">
<style>
  :root {
    --backdrop: #ececec;
    --card: #272a33;
    --gold: #d3a844;
    --gold-light: #f1d27a;
    --gold-deep: #a97e26;
  }
  html, body {
    margin: 0;
    padding: 0;
    width: 1200px;
    height: 857px;
    overflow: hidden;
    background: var(--backdrop);
  }
  .stage {
    position: relative;
    width: 1200px;
    height: 857px;
    overflow: hidden;
    background: var(--backdrop);
  }
  .card-shape {
    position: absolute;
    left: 0;
    top: 0;
  }
  .card-body { fill: var(--card); }
  .rule-line { stroke: var(--gold); }
  .rule-dot { fill: var(--gold); }
  .ornament-placeholder { fill: var(--gold-deep); }
  .brand-name {
    font-family: "Great Vibes", "Brush Script MT", cursive;
    font-weight: 400;
    font-size: 250px;
    fill: var(--gold);
  }
  .tagline {
    position: absolute;
    left: 300px;
    top: 470px;
    margin: 0;
    font-family: "Playfair Display", Georgia, serif;
    font-weight: 700;
    font-size: 17px;
    line-height: 27px;
    text-transform: uppercase;
    color: var(--gold);
    white-space: nowrap;
  }
  .tagline span { display: block; }
  .tagline .line-one { letter-spacing: 12px; }
  .tagline .line-two { letter-spacing: 17px; }
</style>
</head>
<body>
<main class="stage">
  <svg class="card-shape" width="1200" height="857" viewBox="0 0 1200 857">
    <path class="card-body" fill-rule="evenodd" d="
      M237 65 H963 V790 H237 Z
      M497 107 H593 A22 22 0 0 1 637 107 H707 A19 19 0 0 1 707 145 H497 A19 19 0 0 1 497 107 Z
      M325 595 H877 A35 35 0 0 1 912 630 V725 A35 35 0 0 1 877 760 H325 A35 35 0 0 1 290 725 V630 A35 35 0 0 1 325 595 Z"/>

    <g class="rule rule-upper" aria-hidden="true">
      <line class="rule-line" x1="700" y1="301" x2="930" y2="301" stroke-width="2"/>
      <line class="rule-line" x1="712" y1="296" x2="850" y2="296" stroke-width="1"/>
      <circle class="rule-dot" cx="699" cy="301" r="2.5"/>
    </g>

    <text class="brand-name" x="292" y="440">Vexa</text>

    <g class="rule rule-lower" aria-hidden="true">
      <line class="rule-line" x1="270" y1="533" x2="930" y2="533" stroke-width="2"/>
      <line class="rule-line" x1="345" y1="541" x2="855" y2="541" stroke-width="1"/>
      <circle class="rule-dot" cx="270" cy="533" r="2.5"/>
      <circle class="rule-dot" cx="930" cy="533" r="2.5"/>
    </g>
    <rect class="ornament-placeholder" x="588" y="544" width="24" height="24" rx="4"
          role="img" aria-label="Small gold filigree ornament centred under the rule"/>
  </svg>

  <p class="tagline">
    <span class="line-one">100% Premium Virgin</span>
    <span class="line-two">Remy Human Hair</span>
  </p>
</main>
</body>
</html>
```